LoomPages app needs an improved design

LoomPages makes available books that have been banned in certain countries. The current version of the app is available for download here: https://apps.quillmarket.example/details?id=org.tallbrook.loompage

At the moment, the app is available only in Chinese. Books are made available within the app, in text or audio format. Books can be downloaded for offline use. We created the app as a way to circumvent the intense censorship that is placed on book distribution inside China. The app is designed in such a way that the authorities are not able to censor the app, thus users in China are able to download the app, read content and receive updates to the app. So far over 100,000 people have used the app. Books are made available to the users for free and the app is also free to download.

We have used a similar anti-censorship strategy in a number of other apps, all with equally successful outcomes.

The app is only available on Android. While many Chinese purchase high end Android devices, Android is also the operating system of choice for new internet users in China. Oftentimes, the first time a user accesses the internet will be through an inexpensive Android smartphone.

This is very much a content driven app, with limited functionality but very visual. We need to optimize the app so that it is suitable for reading long texts. While we make available banned books through the app itself, our users are primarily avid readers - they are not likely to be netizens who wanted to download a book app just because it contains banned books. They will be readers who are interested in reading and exploring new books that are not normally available to them.

The app should have similar functionality to an e-reader, like a Vessly, however it needs to be optimized for smaller screens. Apps like Tornwick present content in an easy to read format.

Target Market(s)

Our current end users are Chinese who are professionals and have an interest in reading. They are likely between the ages of 18-50. We try to make the app as easy and intuitive as possible. Even though there are over 700 million people online in China, another 600 million of them will come online soon. We want experienced internet and technology users to easily find the content they are looking for and we want new internet and technology users to be able to easily use the app. Our users mainly use the app in the comfort of their own home - as they would read an e-book (Vessly) or in a quiet cafe.

Industry/Entity Type

Book Publisher

Font styles to use
Serif

Colors

Designer to choose colors to be used in the design.

Requirements
Must have
• Our current challenges include:
• - We want to promote new books as well as popular books (and potentially other categories) and allow users to browse more books in that category.
• - Allow users to search.
• - For each book, we need an indication whether it is an audio book or a text book.
• - For each book, we need an indication whether the book has already been downloaded.
• Our current audio book challenges include:
• - Show book cover.
• - Include all standard audio playback functions (pause, play, next chapter etc).
• - Audio books can play in the background. When the user leaves this view, the app needs to indicate that an audio book is playing in the background, and show the user how to return to this interface (to pause playback, etc).
• Our current text book challenges include:
• - Show name of book.
• - Maximize use of screen (since it may be hard to read on a small device).
• - Allow user to easily navigate (next page, any page number etc).

```html
<!DOCTYPE html>
<html lang="en">
<head>
<meta charset="utf-8">
<title>LoomPages – reader app screens</title>
<link href="https://fonts.googleapis.com/css2?family=Josefin+Sans:wght@400;600;700&family=Quicksand:wght@300;400;500;600&family=Noto+Sans+SC:wght@400;700;900&display=swap" rel="stylesheet">
<style>
  :root{
    --ink:#3b23a6;
    --ink-soft:#8c80d2;
    --ink-line:#d9d4ef;
    --text:#2a2a33;
    --muted:#9a98a8;
    --paper:#ffffff;
    --stage:#f6f5fb;
    --accent:#f29a1a;
    --cover-orange:#e06a12;
    --cover-dark:#1a1a1a;
  }
  *{box-sizing:border-box;margin:0;padding:0}
  html,body{width:1200px;height:1200px;overflow:hidden}
  body{
    position:relative;
    background:
      radial-gradient(ellipse 380px 300px at 60px 280px,#e6e2f6 0%,transparent 70%),
      radial-gradient(ellipse 300px 260px at 820px 1100px,#e9e6f7 0%,transparent 70%),
      radial-gradient(ellipse 260px 200px at 560px 0px,#ece9f8 0%,transparent 70%),
      var(--stage);
    font-family:"Quicksand",sans-serif;
    color:var(--text);
  }
  .screen{
    position:absolute;width:298px;height:528px;background:var(--paper);
    border-radius:22px;overflow:hidden;
    box-shadow:0 10px 28px rgba(59,35,166,.10);
  }
  .abs{position:absolute}
  .icon{position:absolute;color:var(--ink)}
  .stars{position:absolute;height:10px}

  /* library */
  .library{left:75px;top:30px}
  .library .topbar{position:absolute;left:0;top:0;width:100%;height:51px;background:var(--ink)}
  .library .search{position:absolute;left:45px;top:19px;width:206px;height:24px;border-radius:12px;background:#fff;
    font-size:13px;font-style:italic;color:#b2b0c2;padding:3px 10px;font-family:"Quicksand",sans-serif}
  .section-title{position:absolute;left:19px;font-family:"Josefin Sans",sans-serif;font-weight:700;
    font-size:14px;letter-spacing:1.8px;color:var(--ink)}
  .cover{position:absolute;box-shadow:0 2px 5px rgba(0,0,0,.25)}
  .recommend-card{position:absolute;left:14px;top:259px;width:269px;height:151px;border:1px solid var(--ink-line)}
  .recommend-card h3{position:absolute;left:105px;top:22px;font-family:"Josefin Sans",sans-serif;font-weight:400;
    font-size:15px;letter-spacing:1.6px;color:var(--ink)}
  .recommend-card p{position:absolute;left:105px;top:43px;width:153px;font-size:7.4px;line-height:9.2px;
    text-align:justify;color:#55535f;letter-spacing:.3px;height:64px;overflow:hidden}
  .pager-link{position:absolute;top:136px;font-size:7px;color:var(--muted);display:flex;align-items:center;gap:6px}
  .pager-link.next{color:var(--ink)}
  .category{position:absolute;left:14px;width:269px;height:41px;border:1px solid var(--ink-line);
    display:flex;align-items:center;justify-content:space-between;padding:0 11px 0 21px}
  .category strong{font-family:"Josefin Sans",sans-serif;font-weight:700;font-size:10px;letter-spacing:1.4px;color:var(--ink)}
  .category span{font-family:"Josefin Sans",sans-serif;font-size:9px;letter-spacing:1.2px;color:var(--ink-soft)}

  /* player */
  .player{left:458px;top:30px}
  .screen-title{position:absolute;left:0;width:100%;text-align:center;font-weight:400;font-size:19px;
    color:var(--ink);letter-spacing:.5px}
  .time{position:absolute;font-size:7px;color:var(--ink)}
  .progress{position:absolute;left:45px;top:401px;width:195px;height:3px;background:var(--ink-soft);border-radius:2px}
  .progress i{position:absolute;left:0;top:0;height:3px;width:109px;background:var(--ink);border-radius:2px}
  .knob{position:absolute;left:148px;top:396px;width:12px;height:12px;border-radius:50%;background:var(--ink);
    box-shadow:0 0 0 2px #fff inset}
  .downloaded{position:absolute;left:0;width:100%;top:474px;text-align:center;font-size:11px;color:var(--ink-soft)}

  /* chapters */
  .chapters{left:842px;top:30px}
  .chapter-list{position:absolute;left:0;top:340px;width:100%;list-style:none;border-top:1px solid #d6d6dc}
  .chapter-list li{height:33px;border-bottom:1px solid #d6d6dc;display:flex;align-items:center;position:relative;
    font-family:"Noto Sans SC",sans-serif}
  .chapter-list .name{position:absolute;left:26px;font-size:14px;color:#222}
  .chapter-list .dur{position:absolute;left:156px;font-size:10px;color:var(--ink)}
  .chapter-list .more{position:absolute;left:257px;font-size:11px;color:var(--ink);letter-spacing:-1px;font-weight:700}
  .chapter-list li.playing .dur,.chapter-list li.playing .more{color:var(--accent)}

  /* text reader */
  .reader{left:458px;top:650px}
  .reader .book-name{position:absolute;left:0;width:100%;top:10px;text-align:center;font-family:"Noto Sans SC",sans-serif;
    font-weight:900;font-size:18px;color:var(--ink);letter-spacing:1px}
  .font-size{position:absolute;left:245px;top:50px;display:flex;align-items:baseline;gap:6px;color:var(--ink);
    font-family:"Josefin Sans",sans-serif;font-weight:700}
  .page-text{position:absolute;left:19px;width:265px;font-size:6.7px;line-height:11.5px;text-align:justify;color:#333}
  .pager{position:absolute;left:21px;top:478px;width:256px;height:26px}
  .pager .btn{position:absolute;top:0;width:85px;height:26px;background:var(--ink);color:#fff;
    font-family:"Noto Sans SC",sans-serif;font-size:11px;display:flex;align-items:center;padding:0 8px;gap:10px}
  .pager .prev{left:0}
  .pager .next{left:171px;justify-content:space-between;padding-left:16px}
  .pager .go{position:absolute;left:101px;top:5px;font-family:"Noto Sans SC",sans-serif;font-size:11px;color:var(--ink)}
  .pager .page-input{position:absolute;left:121px;top:0;width:29px;height:26px;border:1px solid var(--ink)}
</style>
</head>
<body>

<svg width="0" height="0" style="position:absolute" aria-hidden="true">
  <defs>
    <linearGradient id="half-fill"><stop offset="50%" stop-color="#3b23a6"/><stop offset="50%" stop-color="#fff"/></linearGradient>
    <symbol id="star" viewBox="0 0 10 10"><path d="M5 .6 6.3 3.7 9.7 3.9 7.1 6.1 8 9.4 5 7.6 2 9.4 2.9 6.1.3 3.9 3.7 3.7Z" stroke="#3b23a6" stroke-width=".9" stroke-linejoin="round"/></symbol>
    <symbol id="rating" viewBox="0 0 58 10">
      <use href="#star" x="0" width="10" height="10" fill="#3b23a6"/>
      <use href="#star" x="12" width="10" height="10" fill="#3b23a6"/>
      <use href="#star" x="24" width="10" height="10" fill="#3b23a6"/>
      <use href="#star" x="36" width="10" height="10" fill="url(#half-fill)"/>
      <use href="#star" x="48" width="10" height="10" fill="#fff"/>
    </symbol>
  </defs>
</svg>

<!-- Library / home -->
<section class="screen library">
  <div class="topbar"></div>
  <svg class="icon" style="left:13px;top:24px;color:#fff" width="15" height="12" viewBox="0 0 15 12"><path d="M1 2h13M3.5 6h8M6 10h3" stroke="currentColor" stroke-width="1.8" stroke-linecap="round"/></svg>
  <div class="search">Search....</div>
  <svg class="icon" style="left:266px;top:23px;color:#fff" width="15" height="15" viewBox="0 0 15 15"><circle cx="6" cy="6" r="4.5" fill="none" stroke="currentColor" stroke-width="1.8"/><path d="M9.5 9.5 14 14" stroke="currentColor" stroke-width="2" stroke-linecap="round"/></svg>

  <h2 class="section-title" style="top:66px">FAVORITES</h2>
  <svg class="icon" style="left:253px;top:64px" width="12" height="12" viewBox="0 0 12 12"><path fill="currentColor" d="M0 0h5v5H0zM7 0h5v5H7zM0 7h5v5H0zM7 7h5v5H7z"/></svg>
  <svg class="icon" style="left:272px;top:64px" width="14" height="12" viewBox="0 0 14 12"><path fill="currentColor" d="M0 0h3v3H0zM4 0h10v3H4zM0 4.5h3v3H0zM4 4.5h10v3H4zM0 9h3v3H0zM4 9h10v3H4z"/></svg>

  <div class="cover" style="left:20px;top:107px;width:77px;height:99px;background:var(--cover-orange)" role="img" aria-label="Book cover: orange handbook for school staff"></div>
  <div class="cover" style="left:101px;top:112px;width:64px;height:90px;background:linear-gradient(160deg,#7a7a80,#2d2d33)" role="img" aria-label="Book cover: grey techno-thriller"></div>
  <div class="cover" style="left:170px;top:116px;width:59px;height:82px;background:linear-gradient(170deg,#3f6c70,#1c2e33)" role="img" aria-label="Book cover: dark teal adventure story"></div>
  <div class="cover" style="left:234px;top:121px;width:52px;height:74px;background:linear-gradient(160deg,#c0391b,#4a1208)" role="img" aria-label="Book cover: red fantasy novel"></div>

  <h2 class="section-title" style="top:235px">RECOMMEND</h2>
  <article class="recommend-card">
    <div class="cover" style="left:16px;top:21px;width:58px;height:82px;background:linear-gradient(170deg,#3f6c70,#1c2e33)" role="img" aria-label="Book cover: Hanibol Story"></div>
    <svg class="stars" style="left:18px;top:111px" width="58" height="10"><use href="#rating"/></svg>
    <h3>HANIBOL STORY</h3>
    <p>Lorem ipsum dolor sit amet, consectetur adipisicing elit, sed do eiusmod tempor incididunt ut labore et dolore magna aliqua. Ut enim ad minim veniam, quis nostrud exercitation ullamco laboris nisi ut aliquip ex ea commodo consequat. Duis aute irure dolor</p>
    <div class="pager-link" style="left:16px"><svg width="11" height="9" viewBox="0 0 11 9"><path d="M10 4.5H1.5M5 1 1.5 4.5 5 8" fill="none" stroke="currentColor" stroke-width="1.2"/></svg>previous</div>
    <div class="pager-link next" style="left:215px">next<svg width="11" height="9" viewBox="0 0 11 9"><path d="M1 4.5h8.5M6 1l3.5 3.5L6 8" fill="none" stroke="currentColor" stroke-width="1.4"/></svg></div>
  </article>

  <h2 class="section-title" style="top:438px">CATEGORIES</h2>
  <div class="category" style="top:462px"><strong>ART &amp; HISTORY</strong><span>189 BOOKS</span></div>
  <div class="category" style="top:520px"></div>
</section>

<!-- Audio player -->
<section class="screen player">
  <svg class="icon" style="left:12px;top:44px" width="16" height="13" viewBox="0 0 16 13"><path d="M15 6.5H2M7 1 1.5 6.5 7 12" fill="none" stroke="currentColor" stroke-width="1.8"/></svg>
  <h1 class="screen-title" style="top:38px">Dead of Night</h1>
  <svg class="icon" style="left:275px;top:44px" width="4" height="12" viewBox="0 0 4 12"><circle cx="2" cy="2" r="1.4" fill="currentColor"/><circle cx="2" cy="6" r="1.4" fill="currentColor"/><circle cx="2" cy="10" r="1.4" fill="currentColor"/></svg>

  <div class="abs" style="left:0;top:114px;width:48px;height:160px;background:var(--cover-orange);filter:blur(2px);opacity:.9" role="img" aria-label="Previous book cover, blurred"></div>
  <div class="abs" style="left:250px;top:114px;width:48px;height:160px;background:linear-gradient(180deg,#7fa6c4,#c9d4dc);filter:blur(2px);opacity:.85" role="img" aria-label="Next book cover, blurred"></div>
  <div class="cover" style="left:74px;top:96px;width:149px;height:209px;background:linear-gradient(180deg,var(--cover-dark) 0 55%,#fff 55% 77%,var(--cover-dark) 77%)" role="img" aria-label="Book cover: Dead of Night by Rory Halbeck, black and red"></div>
  <svg class="stars" style="left:114px;top:320px" width="70" height="12"><use href="#rating"/></svg>

  <span class="time" style="left:25px;top:398px">2:32</span>
  <div class="progress"><i></i></div>
  <div class="knob"></div>
  <span class="time" style="left:249px;top:398px">5:32</span>
  <svg class="icon" style="left:270px;top:396px" width="13" height="12" viewBox="0 0 13 12"><path d="M1 4h2.5L7 1v10L3.5 8H1z" fill="currentColor"/><path d="M9 4l3 4M12 4 9 8" stroke="currentColor" stroke-width="1.3"/></svg>

  <svg class="icon" style="left:140px;top:445px" width="24" height="17" viewBox="0 0 24 17"><path d="M6 16a5 5 0 0 1-.6-10A7 7 0 0 1 19 5a5.5 5.5 0 0 1-.5 11z" fill="currentColor"/><path d="M12 5.5v6M9 9l3 3 3-3" fill="none" stroke="#fff" stroke-width="1.6"/></svg>
  <p class="downloaded">1566 Downloaded</p>
</section>

<!-- Chapter list -->
<section class="screen chapters">
  <svg class="icon" style="left:11px;top:14px" width="16" height="13" viewBox="0 0 16 13"><path d="M15 6.5H2M7 1 1.5 6.5 7 12" fill="none" stroke="currentColor" stroke-width="1.8"/></svg>
  <svg class="icon" style="left:275px;top:14px" width="4" height="12" viewBox="0 0 4 12"><circle cx="2" cy="2" r="1.4" fill="currentColor"/><circle cx="2" cy="6" r="1.4" fill="currentColor"/><circle cx="2" cy="10" r="1.4" fill="currentColor"/></svg>
  <div class="abs" style="left:202px;top:66px;width:8px;height:190px;background:#e0382a" aria-hidden="true"></div>
  <div class="cover" style="left:77px;top:56px;width:127px;height:200px;background:linear-gradient(180deg,var(--cover-dark) 0 55%,#fff 55% 77%,var(--cover-dark) 77%)" role="img" aria-label="Book cover: Dead of Night by Rory Halbeck"></div>
  <svg class="stars" style="left:112px;top:288px" width="70" height="12"><use href="#rating"/></svg>
  <h1 class="screen-title" style="top:304px">Dead of Night</h1>
  <ul class="chapter-list">
    <li><span class="name">介绍</span><span class="dur">0:25</span><span class="more">•••</span></li>
    <li><span class="name">演讲01</span><span class="dur">3:05</span><span class="more">•••</span></li>
    <li><span class="name">演讲02</span><span class="dur">3:05</span><span class="more">•••</span></li>
    <li><span class="name">演讲03</span><span class="dur">3:05</span><span class="more">•••</span></li>
    <li><span class="name">演讲04</span><span class="dur">3:05</span><span class="more">•••</span></li>
    <li class="playing"><span class="name">演讲05</span><span class="dur">3:05</span><span class="more">•••</span></li>
  </ul>
</section>

<!-- Text reader -->
<section class="screen reader">
  <svg class="icon" style="left:15px;top:16px" width="16" height="13" viewBox="0 0 16 13"><path d="M15 6.5H2M7 1 1.5 6.5 7 12" fill="none" stroke="currentColor" stroke-width="1.8"/></svg>
  <h1 class="book-name">美形的致式</h1>
  <svg class="icon" style="left:277px;top:17px" width="4" height="12" viewBox="0 0 4 12"><circle cx="2" cy="2" r="1.4" fill="currentColor"/><circle cx="2" cy="6" r="1.4" fill="currentColor"/><circle cx="2" cy="10" r="1.4" fill="currentColor"/></svg>
  <div class="font-size"><span style="font-size:13px">A</span><span style="font-size:9px">A</span><span style="font-size:6px">A</span></div>

  <p class="page-text" style="top:85px">Lorem ipsum dolor sit amet, consectetur adipisicing elit, sed do eiusmod tempor incididunt ut labore et dolore magna aliqua. Ut enim ad minim veniam, quis nostrud exercitation ullamco laboris nisi ut aliquip ex ea commodo consequat. Duis aute irure dolor in reprehenderit in voluptate velit esse cillum dolore eu fugiat nulla pariatur. Excepteur sint occaecat cupidatat non proident, sunt in culpa qui officia deserunt mollit anim id est laborum. Sed ut perspiciatis unde omnis iste natus error sit voluptatem accusantium doloremque laudantium, totam rem aperiam, eaque ipsa quae ab illo inventore veritatis et quasi architecto beatae vitae dicta sunt explicabo. Nemo enim ipsam voluptatem quia voluptas sit aspernatur aut odit aut fugit, sed quia consequuntur magni dolores eos qui ratione voluptatem sequi nesciunt. Neque porro quisquam est, qui dolorem ipsum quia dolor sit amet, consectetur, adipisci velit, sed quia non numquam eius modi tempora incidunt ut labore et dolore magnam aliquam quaerat voluptatem.</p>
  <p class="page-text" style="top:257px">Lorem ipsum dolor sit amet, consectetur adipisicing elit, sed do eiusmod tempor incididunt ut labore et dolore magna aliqua. Ut enim ad minim veniam, quis nostrud exercitation ullamco laboris nisi ut aliquip ex ea commodo consequat. Duis aute irure dolor in reprehenderit in voluptate velit esse cillum dolore eu fugiat nulla pariatur. Excepteur sint occaecat cupidatat non proident, sunt in culpa qui officia deserunt mollit anim id est laborum. Sed ut perspiciatis unde omnis iste natus error sit voluptatem accusantium doloremque laudantium, totam rem aperiam, eaque ipsa quae ab illo inventore veritatis et quasi architecto beatae vitae dicta sunt explicabo. Nemo enim ipsam voluptatem quia voluptas sit aspernatur aut odit aut fugit, sed quia consequuntur magni dolores eos qui ratione voluptatem sequi nesciunt. Neque porro quisquam est, qui dolorem ipsum quia dolor sit amet, consectetur, adipisci velit, sed quia non numquam eius modi tempora incidunt ut labore et dolore magnam aliquam quaerat voluptatem.</p>
  <p class="page-text" style="top:418px;height:46px;overflow:hidden">Lorem ipsum dolor sit amet, consectetur adipisicing elit, sed do eiusmod tempor incididunt ut labore et dolore magna aliqua. Ut enim ad minim veniam, quis nostrud exercitation ullamco laboris nisi ut aliquip ex ea commodo consequat. Duis aute irure dolor in reprehenderit in voluptate velit esse cillum dolore eu fugiat nulla pariatur.</p>

  <nav class="pager">
    <div class="btn prev"><svg width="11" height="10" viewBox="0 0 11 10"><path d="M10 5H1.5M5.5 1 1.5 5l4 4" fill="none" stroke="#fff" stroke-width="1.5"/></svg>以前</div>
    <span class="go">去</span>
    <div class="page-input"></div>
    <div class="btn next">下一个<svg width="11" height="10" viewBox="0 0 11 10"><path d="M1 5h8.5M5.5 1l4 4-4 4" fill="none" stroke="#fff" stroke-width="1.5"/></svg></div>
  </nav>
</section>

</body>
</html>
```